Resume for CEO

I need two formats of a resume created.

#1. It is 3 pages long and is the extended version.

#2. Is the 1 page resume.

Both should have the same styling. I am attaching the long and short version in word. I am also attaching a temporary picture for the resume. I will switch that out myself. Don't worry about keeping the sizing. It can be whatever you want.

There is a good website to use as a reference. http://quillpagecraft.com/
The reason I am not using this site is because they don't give you the files for editing. They make you use them to edit.

Please feel free to ask questions. I"m excited to see the ideas that come up.

End format should be in AI with PDF's. I want 1 resume that is 3-4 pages and one that is 1 page. They should have the same style.

Dale

Reason: I have only received 2 designs. Hopefully I can get more submissions.

Reason: I need to get the design finalized and I will end the project.

```html
<!DOCTYPE html>
<html lang="en">
<head>
<meta charset="utf-8">
<title>Daniel R. Hartwell – Resume Set</title>
<link rel="stylesheet" href="https://fonts.googleapis.com/css2?family=Libre+Baskerville:wght@700&family=Arimo:wght@400;700&display=swap">
<style>
:root{
  --green:#1b6b3b;
  --green-dark:#155a30;
  --ink:#1d1d1d;
  --grey:#e9e9e9;
  --rule:#cfcfcf;
  --backdrop:#ececec;
}
*{box-sizing:border-box;margin:0;padding:0}
html,body{width:1050px;height:1200px;overflow:hidden;background:var(--backdrop)}
body{position:relative;font-family:"Arimo",Arial,sans-serif;color:var(--ink)}
.page{position:absolute;background:#fff;box-shadow:2px 3px 7px rgba(0,0,0,.35);overflow:hidden}
.page-foot{position:absolute;left:0;right:0;bottom:0;background:var(--green);color:#fff;font-weight:700;text-align:center;display:flex;flex-direction:column;justify-content:center}
.block{position:absolute}
.name{font-family:"Libre Baskerville",Georgia,serif;font-weight:700;color:var(--green);text-align:center;left:0;right:0;white-space:nowrap;line-height:1.1;text-shadow:1px 2px 2px rgba(0,0,0,.25)}
.title-line{left:0;right:0;display:flex;justify-content:center;align-items:center;font-weight:700;letter-spacing:.6px;white-space:nowrap}
.title-line .dots{border-top:3px dotted var(--green);margin:0 12px}
.sec{position:absolute;display:flex;height:18px;border-bottom:2px solid var(--green)}
.sec .tab{background:var(--green);color:#fff;font-family:"Libre Baskerville",Georgia,serif;font-weight:700;font-size:8px;letter-spacing:.4px;padding:0 16px 0 9px;display:flex;align-items:center;clip-path:polygon(0 0,100% 0,calc(100% - 10px) 100%,0 100%);margin-right:-8px;position:relative;z-index:1}
.sec .rest{flex:1;background:linear-gradient(#f4f4f4,#cfcfcf);color:var(--green);font-family:"Libre Baskerville",Georgia,serif;font-weight:700;font-size:8px;letter-spacing:.4px;padding-left:10px;display:flex;align-items:center}
.sec.small{height:14px}
.sec.small .tab,.sec.small .rest{font-size:6.2px}
.frame{position:absolute;border:1px solid var(--rule)}
.photo{position:absolute;background:linear-gradient(160deg,#b99a62 0%,#6b5436 40%,#2b2d33 75%,#1c1d22 100%);box-shadow:1px 2px 4px rgba(0,0,0,.4)}
.txt{line-height:1.32}
.txt p{margin-bottom:5px}
.job h4{font-weight:700;font-size:1.12em}
.job .when{font-style:italic;margin-bottom:4px}
.job .co{margin-bottom:4px}
.bold{font-weight:700}
.dotsep{border-top:2.5px dotted var(--green);margin:6px auto}
.bullets{list-style:none}
.bullets li{position:relative;padding-left:8px;margin-bottom:4px}
.bullets li::before{content:"";position:absolute;left:1px;top:.5em;width:3px;height:3px;border-radius:50%;background:var(--ink)}
.caps{list-style:none;font-weight:700;text-transform:uppercase}
.caps li{position:relative;padding-left:7px;margin-bottom:2.6px}
.caps li::before{content:"";position:absolute;left:0;top:.4em;width:2.6px;height:2.6px;background:var(--ink)}
.ka{font-weight:700;margin-bottom:4px}
.vrule{position:absolute;border-left:1px solid var(--rule)}
</style>
</head>
<body>

<!-- Page two of extended resume -->
<section class="page" style="left:524px;top:586px;width:376px;height:486px;font-size:5.6px">
  <div class="frame" style="left:24px;top:30px;width:333px;height:408px"></div>
  <div class="sec small" style="left:24px;top:30px;width:333px"><span class="tab">PROFESSIONAL</span><span class="rest">EXPERIENCE</span></div>
  <div class="block txt job" style="left:33px;top:50px;width:142px">
    <h4>Interim Chief Executive Officer</h4>
    <div class="when">August 2013 – January 2014</div>
    <div class="co">Melted Crust Truck Co.: Austin, TX<br>(www.meltedcrusttruck.com)</div>
    <p>Provides strategic direction as Interim CEO for this innovative gourmet food truck company aiming to be the first publicly traded gourmet food truck company in the United States. Challenged to prove franchise model in Texas as first master franchise market in order to prove model successful to secure anticipated Initial Public Offering.</p>
  </div>
  <div class="block txt" style="left:187px;top:50px;width:165px">
    <div class="ka">KEY ACHIEVEMENTS:</div>
    <ul class="bullets">
      <li>Launched company in post-acquisition growing organization, while establishing and integrating the truck brand.</li>
      <li>Accelerated company into explosive revenue increase of 100% month over month.</li>
      <li>Designed new sales and booking systems in order to build strong foundational sales program.</li>
      <li>Developed fresh accounting department in addition to establishing systems and acquiring key management.</li>
    </ul>
  </div>
  <div class="block dotsep" style="left:60px;top:146px;width:260px"></div>
  <div class="block txt job" style="left:33px;top:158px;width:142px">
    <h4>Chief Executive Officer</h4>
    <div class="when">May 2009 – November 2011</div>
    <div class="co">Ashford Handbuilt Cycles, Inc.: San Diego, CA (www.ashfordcycles.com)</div>
    <p>Served as CEO during strong economic downturn. Business was suffering from significant revenue loss, declining employee morale, and ineffective organizational strategy. Deployment of key management, static growth, and implementation of dynamic systems were key to the stabilization of this organization. As CEO, effectively returned the company to profitability within 12 months by implementing efficiencies, modifying manufacturing protocol, rebranding corporate image, improving marketing and sales strategies, and renovating its philosophy and framework.</p>
  </div>
  <div class="block txt" style="left:187px;top:158px;width:165px">
    <div class="ka">KEY ACHIEVEMENTS:</div>
    <ul class="bullets">
      <li>Acquired and established new healthy, efficient, cost effective management team and leadership providing strategic operational and financial company direction.</li>
      <li>Implemented ERP system, establishing accurate inventory controls and manufacturing cost accounting measurements to accurately calculate cost of goods.</li>
      <li>Designed inventory aging metric in conjunction with velocity reporting to improve inventory capital requirements, inventory turns and just in time strategies.</li>
      <li>Rebranded company image and implemented new sales and marketing strategy resulting in strong revenue increase.</li>
      <li>Exceeded pre-downturn figures within 12 months accelerating company into strong trajectory for success.</li>
    </ul>
  </div>
  <div class="sec small" style="left:24px;top:308px;width:333px"><span class="tab">ENTREPRENEURIAL</span><span class="rest">EXPERIENCE</span></div>
  <div class="block txt job" style="left:33px;top:328px;width:145px">
    <h4>Co- Founder &amp; Chief Executive Officer</h4>
    <div class="when">January 2011 – Present</div>
    <div class="co">Northgate Media, Inc.: San Diego, CA</div>
    <p>Serves as Co-Founder and CEO for this marketing, media, branding, public relation, and corporate consulting company. Northgate Media provides valuable resources to public, private, and non-profit sector organizations across multiple mediums. Provides strategic direction and subject matter expertise working directly with diverse clientele. Negotiates contracts as needed as well as organizes and manages projects and contractors.</p>
  </div>
  <div class="block txt" style="left:197px;top:330px;width:160px">
    <div class="ka">CORE SERVICES PROVIDED:</div>
    <div style="display:flex;gap:8px">
      <ul class="bullets" style="width:62px"><li>Branding</li><li>Event Planning</li><li>Graphic Arts</li><li>Marketing</li><li>Photography</li><li>Public Relations</li><li>Publishing</li></ul>
      <ul class="bullets"><li>Reputation Management</li><li>SEO</li><li>Social Media</li><li>Video Creation</li><li>Web Design</li><li>Writing Services</li></ul>
    </div>
  </div>
  <div class="page-foot" style="height:32px"></div>
</section>

<!-- One-page resume (large) -->
<section class="page" style="left:70px;top:30px;width:486px;height:630px;font-size:7.1px">
  <h1 class="block name" style="top:22px;font-size:31px">DANIEL R. HARTWELL</h1>
  <div class="block title-line" style="top:64px;font-size:12.5px"><span class="dots" style="width:36px"></span>CHIEF EXECUTIVE OFFICER &nbsp;/&nbsp; ENTREPRENEUR<span class="dots" style="width:36px"></span></div>
  <div class="frame" style="left:25px;top:92px;width:436px;height:490px"></div>
  <div class="sec" style="left:25px;top:92px;width:436px"><span class="tab">PROFILE</span><span class="rest"></span></div>
  <p class="block txt" style="left:38px;top:121px;width:298px">Dynamic Chief Executive Officer with over 16 years of experience in providing strategic direction and leadership for organizations in multiple markets with unique situations. Extensive experience transforming companies into profitable and progressive organizations using proven systematic implementation. Offers comprehensive knowledge and operational experience with highly-engineered technical manufacturing companies, ecommerce and international brand building. Effectively identifies critical business drivers in multiple markets and industries, enabling growth opportunities within a variety of departments and ultimately complete business expansion.</p>
  <div class="photo" role="img" aria-label="Portrait photo of the candidate in a dark suit" style="left:348px;top:122px;width:102px;height:131px"></div>
  <div class="sec" style="left:25px;top:200px;width:308px"><span class="tab">SKILLS</span><span class="rest"></span></div>
  <p class="block txt bold" style="left:38px;top:227px;width:305px;line-height:1.48">CEO &nbsp;•&nbsp; LEADERSHIP &amp; VISION &nbsp;•&nbsp; TURNAROUND &nbsp;•&nbsp; CORPORATE RESTRUCTURING<br>BRAND BUILDING &nbsp;•&nbsp; PRODUCT DEVELOPMENT &amp; CONTRACT MANUFACTURING<br>STRONG FINANCIAL ACCOUNTING &nbsp;•&nbsp; SALES &amp; MARKETING STRATEGIC PLANNING</p>
  <div class="sec" style="left:25px;top:267px;width:211px"><span class="tab">PROFESSIONAL</span><span class="rest">EXPERIENCE</span></div>
  <div class="sec" style="left:252px;top:267px;width:209px"><span class="tab">ENTREPRENEURIAL</span><span class="rest">EXPERIENCE</span></div>
  <div class="vrule" style="left:244px;top:292px;height:280px"></div>
  <div class="block txt job" style="left:38px;top:293px;width:196px">
    <h4>Interim Chief Executive Officer</h4>
    <div class="when">August 2013 – January 2014</div>
    <div class="co">Melted Crust Truck Co.: Austin, TX<br>(www.meltedcrusttruck.com)</div>
    <p>Provides strategic direction as Interim CEO for this innovative gourmet food truck company aiming to be the first publicly traded gourmet food truck company in the United States.</p>
    <div class="dotsep" style="width:130px"></div>
    <h4>Chief Executive Officer</h4>
    <div class="when">May 2009 – November 2011</div>
    <div class="co">Ashford Handbuilt Cycles, Inc.: San Diego, CA<br>(www.ashfordcycles.com)</div>
    <p>Turned this ailing specialty bicycle company around through rebranding efforts and improved marketing and sales strategy, accelerating to profitable state within 12 months.</p>
  </div>
  <div class="block txt job" style="left:258px;top:292px;width:198px;font-size:6.5px;line-height:1.28">
    <h4>Co- Founder &amp; Chief Executive Officer</h4>
    <div class="when">January 2011 – Present</div>
    <div class="co">Northgate Media, Inc.: San Diego, CA</div>
    <p>Serves as Co-Founder and CEO for this marketing, media, branding, public relation, and corporate consulting company providing valuable resources to public, private, and non-profit sector organizations.</p>
    <div class="dotsep" style="width:130px"></div>
    <h4>Founder &amp; Chief Executive Officer</h4>
    <div class="when">May 2009 – Present</div>
    <div class="co">Keystone Precision, Inc.: San Diego, CA<br>(www.keystoneprecision.com)</div>
    <p>Founded this cutting-edge company, redefining the level of technology, quality, and product weight in the bicycle component segment of the cycling industry launching toward international distribution and representation in 23 countries.</p>
    <div class="dotsep" style="width:130px"></div>
    <h4>Founder &amp; Chief Executive Officer</h4>
    <div class="when">December 1999 – April 2009</div>
    <div class="co">Farther Trails, Inc.: San Diego, CA</div>
    <p>Farther Trails, Inc. experienced explosive revenue growth fueled by strategic purchasing partnerships, aggressive sales and marketing techniques, and new cutting-edge ecommerce technology implementation. Following the development of new verticals, watersports, and camping, Farther Trails was acquired after becoming one of the nation's largest e-commerce, mail-order, brick and mortar specialty retailers. Purchased by Petwell Group, Inc. in 2009 by owners of tailandtrail.com.</p>
  </div>
  <div class="sec" style="left:25px;top:470px;width:211px"><span class="tab">EDUCATION</span><span class="rest"></span></div>
  <div class="block txt" style="left:38px;top:499px;width:206px;font-size:6.8px">
    <p><span class="bold">General Studies &amp; Pre-Med</span><br>Seaview University</p>
    <p><span class="bold" style="white-space:nowrap">Bachelor of Science in Business Administration/Marketing</span><br>Pacific Coast University</p>
  </div>
  <div class="page-foot" style="height:40px;font-size:10px;line-height:1.55">
    <span>4810 Harbor Crest Dr. Ste. 210 &nbsp;•&nbsp; San Diego, CA 92130</span>
    <span>(619) 555-0142 &nbsp;•&nbsp; dhartwell@example.com</span>
  </div>
</section>

<!-- Page one of extended resume -->
<section class="page" style="left:595px;top:87px;width:375px;height:486px;font-size:6.2px">
  <h1 class="block name" style="top:16px;font-size:24px">DANIEL R. HARTWELL</h1>
  <div class="block title-line" style="top:50px;font-size:10.5px"><span class="dots" style="width:26px"></span>CHIEF EXECUTIVE OFFICER &nbsp;/&nbsp; ENTREPRENEUR<span class="dots" style="width:26px"></span></div>
  <div class="frame" style="left:20px;top:70px;width:335px;height:377px"></div>
  <div class="sec small" style="left:20px;top:70px;width:335px"><span class="tab">PROFILE</span><span class="rest"></span></div>
  <p class="block txt" style="left:32px;top:97px;width:210px">Dynamic Chief Executive Officer with over 16 years of experience in providing strategic direction and leadership for organizations in multiple markets with unique situations. Extensive experience transforming companies into profitable and progressive organizations using proven systematic implementation. Offers comprehensive knowledge and operational experience with highly-engineered technical manufacturing companies, ecommerce and international brand building. Effectively identifies critical business drivers in multiple markets and industries, enabling growth opportunities within a variety of departments and ultimately complete business expansion.</p>
  <div class="photo" role="img" aria-label="Portrait photo of the candidate in a dark suit" style="left:251px;top:94px;width:77px;height:101px"></div>
  <div class="sec small" style="left:20px;top:205px;width:162px"><span class="tab">CAREER</span><span class="rest">ACHIEVEMENTS</span></div>
  <div class="vrule" style="left:187px;top:222px;height:210px"></div>
  <ul class="block txt bullets" style="left:28px;top:227px;width:155px;font-size:5.9px">
    <li>Constructed multiple start-up companies from ground-up utilizing organic growth strategies with little capital demonstrating consistent expansions and sales increase, accelerating into well-known international brands.</li>
    <li>Corporate restructuring and turnaround deployment, assisting several companies from decline and near insolvency into profitable states by streamlining the organization and renovating management, marketing, and sales strategies.</li>
    <li>Produced measurable year-after-year improvement under shifting conditions and economically depressed markets by adopting “lean mentality” and “just-in-time” strategies.</li>
    <li>Conceived and led revenue capture strategies, successfully achieving positive sales trajectories in addition to designing and sourcing innovative and industry-altering technologies.</li>
    <li>Rebuilt and rejuvenated leadership staff into unified, top-performing, and highly motivated teams. Utilizing these teams to secure strong international distribution by expanding businesses into international markets.</li>
  </ul>
  <div class="sec small" style="left:194px;top:205px;width:161px"><span class="tab">CORE</span><span class="rest">COMPETENCIES</span></div>
  <ul class="block caps" style="left:202px;top:226px;width:150px;font-size:5.4px">
    <li>Chief Executive Officer</li><li>Turnaround</li><li>Organic Business Growth</li><li>Brand Building</li><li>Business Development</li><li>Contract Manufacturing</li><li>Strong Financial Accounting</li><li>Corporate Restructuring</li><li>Strategic Sales Planning</li><li>Key Management Construction</li><li>Marketing Strategies</li>
  </ul>
  <div class="sec small" style="left:194px;top:332px;width:161px"><span class="tab">INDUSTRY</span><span class="rest">SPECIALIZATIONS</span></div>
  <ul class="block caps" style="left:202px;top:353px;width:150px;font-size:5.4px">
    <li>International Business</li><li>Outdoor Sporting Goods &amp; Action Sports</li><li>Ecommerce &amp; Specialty Retail</li><li>Int. Distribution &amp; Logistics</li><li>Sales &amp; Marketing Strategies</li><li>Acquisitions &amp; Integrations</li><li>Corporate Funding</li><li>Corporate Restructuring</li>
  </ul>
  <div class="page-foot" style="height:33px;font-size:7.4px;line-height:1.5">
    <span>4810 Harbor Crest Dr. Ste. 210 - San Diego, CA 92130</span>
    <span>(619) 555-0142 - dhartwell@example.com</span>
  </div>
</section>

<!-- Page three of extended resume -->
<section class="page" style="left:113px;top:677px;width:377px;height:486px;font-size:5.6px">
  <div class="frame" style="left:22px;top:30px;width:333px;height:412px"></div>
  <div class="sec small" style="left:22px;top:30px;width:333px"><span class="tab">ENTREPRENEURIAL</span><span class="rest">EXPERIENCE</span></div>
  <div class="block txt job" style="left:35px;top:50px;width:140px">
    <h4>Founder &amp; Chief Executive Officer</h4>
    <div class="when">May 2009 – Present</div>
    <div class="co">Keystone Precision, Inc.: San Diego, CA<br>(www.keystoneprecision.com)</div>
    <p>Founded this forward-thinking, cutting-edge American entrepreneurial start-up company focused on designing, manufacturing and providing the finest bicycle components in the industry. Keystone Precision, Inc. has redefined the level of technology, quality, and product weight in the bicycle component segment of cycling industry leading to strong international brand awareness and distribution. Provided direction, financial acumen, and innovation for this young organization since its inception.</p>
  </div>
  <div class="block txt" style="left:186px;top:62px;width:165px">
    <div class="ka">KEY ACHIEVEMENTS:</div>
    <ul class="bullets">
      <li>Developed cutting-edge technology by outsourcing design, development, and contract manufacturing in Asia.</li>
      <li>Spurred this ground-floor start-up to gaining international brand awareness, attention, and acclaim.</li>
      <li>Achieved international brand representation in over 23+ countries by implementing international distribution strategies.</li>
      <li>Demonstrated explosive revenue growth through utilization of solid domestic sales strategies.</li>
      <li>Designed highly efficient inventory management systems and controls, including automatic min/max, velocity reporting, and inventory aging matrix – a resource crucial for “just-in-time” manufacturing strategy.</li>
      <li>Implemented international and domestic marketing and branding campaign strategy and execution.</li>
    </ul>
  </div>
  <div class="block dotsep" style="left:50px;top:206px;width:270px"></div>
  <div class="block txt job" style="left:35px;top:222px;width:140px">
    <h4>Founder &amp; Chief Executive Officer</h4>
    <div class="when">December 1999 – April 2009</div>
    <div class="co">Farther Trails, Inc.: San Diego, CA</div>
    <p>Founded Farther Trails, Inc., operator of fartherbikes.com, fartherwater.com &amp; farthertrails.com. Farther Trails, Inc. experienced explosive revenue growth fueled by strategic purchasing partnerships, aggressive sales and marketing techniques, and new cutting-edge ecommerce technology implementation. Following the development of new verticals, watersports, and camping, Farther Trails was acquired after becoming one of the nation's largest e-commerce, mail-order, brick and mortar specialty retailers. Purchased by Petwell Group, Inc. in 2009 by owners of tailandtrail.com.</p>
  </div>
  <div class="block txt" style="left:186px;top:222px;width:165px">
    <div class="ka">KEY ACHIEVEMENTS:</div>
    <ul class="bullets">
      <li>Accelerated exponential revenue growth utilizing well-executed organic expansion strategy.</li>
      <li>Began with no capital and grew into multi-million dollar retail company.</li>
      <li>Deployed cutting-edge e-commerce technology as well as highly efficient inventory management software. Leading to: effective inventory turns, inventory aging strategies and product gross margin analysis and catalog management.</li>
      <li>Implemented systems supporting high-velocity, very low margin shopping transactions – processed 300 to 500 packages per day with efficiency and low error margin.</li>
      <li>Developed purchasing and product acquisitions allowing the company to thrive.</li>
      <li>Established and secured strategic partnerships with vital suppliers and vendors.</li>
    </ul>
  </div>
  <div class="sec small" style="left:22px;top:392px;width:333px"><span class="tab">EDUCATION</span><span class="rest"></span></div>
  <div class="block txt" style="left:42px;top:414px;width:120px"><span class="bold">General Studies &amp; Pre-Med</span><br>Seaview University</div>
  <div class="block txt" style="left:166px;top:414px;width:185px"><span class="bold">Bachelor of Science in Business Administration/Marketing</span><br>Pacific Coast University</div>
  <div class="page-foot" style="height:33px"></div>
</section>

</body>
</html>
```